Business Card Design Project

A business card for a new company in Ontario Canada called Build for Growth. It is a consulting company which uses Brixo as the medium for facilitation.

The target market is for senior leaders in healthcare and social services.

Industry/Entity Type

Healthcare

Requirements
Must have
• The name Build For Growth
Dana Montreuil RRT, B Ed (AD ed).
Tacticraft Facililitator (R)

Tag Line
Engaging Transforming and Innovative
The attached logo

danamontreuil@examplemail.com
416-555-0147
Should not have
• Lime green
Times New Roman or Arial font
Do not include Brixo bricks on the card.

```html
<!DOCTYPE html>
<html lang="en">
<head>
<meta charset="UTF-8">
<title>Build for Growth — Business Card</title>
<link href="https://fonts.googleapis.com/css2?family=Architects+Daughter&family=Open+Sans:wght@400;600;700&display=swap" rel="stylesheet">
<style>
  :root {
    --page-bg: #f4f4f4;
    --card-white: #ffffff;
    --blue-top: #3ea4df;
    --blue-bottom: #6fcbf8;
    --purple: #662d91;
    --name-blue: #1b6aa5;
    --ink: #2a2a2a;
    --white: #ffffff;
  }
  * { margin: 0; padding: 0; box-sizing: border-box; }
  html, body {
    width: 1200px;
    height: 900px;
    overflow: hidden;
    background: var(--page-bg);
  }
  .stage {
    width: 1200px;
    height: 900px;
    display: flex;
    align-items: center;
    justify-content: center;
  }
  .business-card {
    position: relative;
    width: 900px;
    height: 514px;
    border-radius: 44px;
    overflow: hidden;
    background: var(--card-white);
    box-shadow: 0 6px 18px rgba(0, 0, 0, 0.18);
  }
  .card-shapes {
    position: absolute;
    inset: 0;
  }
  .tagline {
    position: absolute;
    font-family: "Architects Daughter", cursive;
    font-size: 25px;
    letter-spacing: 2px;
    color: var(--white);
    text-transform: uppercase;
    white-space: nowrap;
  }
  .tagline--engaging { left: 150px; top: 92px; }
  .tagline--transforming { left: 62px; top: 158px; }
  .tagline--innovative { left: 78px; top: 224px; }

  .holder {
    position: absolute;
    left: 78px;
    top: 336px;
    font-family: "Open Sans", sans-serif;
  }
  .holder__name {
    font-size: 19px;
    font-weight: 700;
    color: var(--white);
    white-space: nowrap;
  }
  .holder__title {
    font-size: 17px;
    font-weight: 700;
    color: var(--name-blue);
    margin-top: 2px;
  }
  .contact-list {
    list-style: none;
    margin-top: 20px;
  }
  .contact-list li {
    display: flex;
    align-items: center;
    gap: 14px;
    font-size: 13px;
    font-weight: 600;
    color: var(--white);
    margin-bottom: 6px;
  }
  .contact-icon {
    width: 20px;
    height: 14px;
    flex: none;
  }

  .brand-name {
    position: absolute;
    left: 470px;
    width: 400px;
    top: 236px;
    text-align: center;
    font-family: "Open Sans", sans-serif;
    font-weight: 700;
    font-size: 34px;
    color: var(--ink);
    white-space: nowrap;
  }
</style>
</head>
<body>
  <main class="stage">
    <article class="business-card">
      <svg class="card-shapes" width="900" height="514" viewBox="0 0 900 514" aria-hidden="true">
        <defs>
          <linearGradient id="blueField" x1="0" y1="0" x2="0" y2="1">
            <stop offset="0" style="stop-color: #3ea4df"/>
            <stop offset="1" style="stop-color: #6fcbf8"/>
          </linearGradient>
        </defs>
        <path class="blue-field" d="M0,0 L328,0 C336,200 400,380 530,514 L0,514 Z" fill="url(#blueField)"/>
        <path class="purple-swoosh" d="M344,0 L384,0 C374,160 400,300 470,428 C398,330 352,180 344,0 Z" fill="#662d91"/>
      </svg>

      <p class="tagline tagline--engaging">Engaging</p>
      <p class="tagline tagline--transforming">Transforming</p>
      <p class="tagline tagline--innovative">and Innovative</p>

      <section class="holder">
        <h1 class="holder__name">Dana Montreuil RRT,B Ed(AD ed)</h1>
        <h2 class="holder__title">Tacticraft Facililitator</h2>
        <ul class="contact-list">
          <li>
            <svg class="contact-icon" viewBox="0 0 20 14" aria-hidden="true">
              <rect x="0.5" y="0.5" width="19" height="13" fill="#662d91"/>
              <path d="M1,1 L10,8 L19,1" fill="none" stroke="#ffffff" stroke-width="1.2"/>
            </svg>
            <span>danamontreuil@examplemail.com</span>
          </li>
          <li>
            <svg class="contact-icon" viewBox="0 0 20 14" aria-hidden="true">
              <path d="M1,4 Q10,-1 19,4 L17,6 L14,5 L14,3.5 Q10,2.5 6,3.5 L6,5 L3,6 Z" fill="#662d91"/>
              <path d="M5,6 L15,6 L18,13 L2,13 Z" fill="#662d91"/>
              <circle cx="10" cy="9.5" r="1.6" fill="#ffffff"/>
            </svg>
            <span>416-555-0147</span>
          </li>
        </ul>
      </section>

      <p class="brand-name">Build for Growth</p>
    </article>
  </main>
</body>
</html>
```